Coffee bag stamp design for new coffee brand

Stamp design that will be used like a label on a coffee package.
It must be a vector that can be produced as a stamp. Coffee bag is from brown craft paper. I upload image of this bag. Size of design is 80mm x 140mm.
I also uploaded two pictures for inspiration, but I will also appreciate new ideas.

Target Market(s)

Coffee lovers, who love to try new coffee. Also hipsters.

Colors

Designer to choose only greyscale colors for use in the design.

Requirements
Must have
• Some information about coffee must have:
Name: BRAZIL (the biggest font in that design)
Region: Santos
Altitude: 60 – 1200 m.n.m.
Variety: Arabica
Processing: unwashed

```html
<!DOCTYPE html>
<html lang="en">
<head>
<meta charset="utf-8">
<title>Brazil – Coffee Bag Stamp</title>
<link rel="stylesheet" href="https://fonts.googleapis.com/css2?family=Oswald:wght@300;400;500;600;700&display=swap">
<style>
  :root {
    --paper: #ffffff;
    --kraft: #b89c7c;
    --kraft-dark: #9c8162;
    --ink: #000000;
  }
  html, body {
    margin: 0;
    padding: 0;
    width: 708px;
    height: 1200px;
    overflow: hidden;
    background: var(--paper);
  }
  .label {
    position: relative;
    width: 708px;
    height: 1200px;
    font-family: "Oswald", sans-serif;
  }
  .label__ground {
    position: absolute;
    left: 26px; top: 26px;
    width: 654px; height: 1144px;
    background: var(--kraft);
  }
  .label__frame {
    position: absolute;
    left: 71px; top: 25px;
    width: 565px; height: 1080px;
    border: 2px solid var(--ink);
    box-sizing: border-box;
  }
  .bean-sack-art {
    position: absolute;
    left: 73px; top: 510px;
    width: 561px; height: 593px;
    background: linear-gradient(180deg, rgba(156,129,98,0.55) 0%, rgba(156,129,98,0.25) 55%, rgba(120,98,74,0.5) 100%);
  }
  .grunge-edge {
    position: absolute;
    top: 27px;
    width: 40px; height: 500px;
  }
  .grunge-edge--left {
    left: 160px;
    background: linear-gradient(90deg, rgba(0,0,0,0) 0%, rgba(0,0,0,0.55) 100%);
  }
  .grunge-edge--right {
    left: 510px;
    background: linear-gradient(270deg, rgba(0,0,0,0) 0%, rgba(0,0,0,0.55) 100%);
  }
  .brand-band {
    position: absolute;
    left: 200px; top: 25px;
    width: 310px; height: 536px;
    background: var(--ink);
  }
  .brand-name {
    position: absolute;
    left: 200px; top: 272px;
    width: 310px;
    margin: 0;
    text-align: center;
    color: var(--kraft);
    font-size: 28px;
    font-weight: 600;
    letter-spacing: 2px;
    line-height: 1;
  }
  .info-card {
    position: absolute;
    left: 200px; top: 561px;
    width: 310px; height: 476px;
    background: var(--kraft);
    border: 2px solid var(--ink);
    box-sizing: border-box;
  }
  .info-card__title {
    height: 142px;
    margin: 0;
    display: flex;
    align-items: center;
    justify-content: center;
    font-size: 86px;
    font-weight: 600;
    letter-spacing: 1px;
    color: var(--ink);
    border-bottom: 2px solid var(--ink);
    box-sizing: border-box;
  }
  .spec-row {
    position: relative;
    display: flex;
    align-items: center;
    border-bottom: 2px solid var(--ink);
    box-sizing: border-box;
    color: var(--ink);
  }
  .spec-row:last-child { border-bottom: none; }
  .spec-row--h77 { height: 77px; }
  .spec-row--h88 { height: 88px; }
  .spec-row--h90 { height: 90px; }
  .spec-row--h76 { height: 76px; }
  .spec-row__label {
    position: absolute;
    left: 15px;
    font-size: 21px;
    font-weight: 300;
  }
  .spec-row__divider {
    position: absolute;
    left: 116px;
    width: 3px; height: 30px;
    background: var(--ink);
  }
  .spec-row__value {
    position: absolute;
    left: 146px;
    font-size: 22px;
    font-weight: 500;
    text-transform: uppercase;
  }
</style>
</head>
<body>
<main class="label">
  <div class="label__ground"></div>
  <div class="bean-sack-art" role="img" aria-label="Hand-drawn illustration of a burlap sack overflowing with roasted coffee beans"></div>
  <div class="grunge-edge grunge-edge--left" role="img" aria-label="Distressed ink texture along the edge of the black band"></div>
  <div class="grunge-edge grunge-edge--right" role="img" aria-label="Distressed ink texture along the edge of the black band"></div>
  <div class="label__frame"></div>

  <div class="brand-band"></div>
  <p class="brand-name">NORTHWOOD COFFEE</p>

  <section class="info-card">
    <h1 class="info-card__title">BRAZIL</h1>
    <div class="spec-row spec-row--h77">
      <span class="spec-row__label">variety</span>
      <span class="spec-row__divider"></span>
      <span class="spec-row__value">Arabica</span>
    </div>
    <div class="spec-row spec-row--h88">
      <span class="spec-row__label">region</span>
      <span class="spec-row__divider"></span>
      <span class="spec-row__value">Santos</span>
    </div>
    <div class="spec-row spec-row--h90">
      <span class="spec-row__label">altitude</span>
      <span class="spec-row__divider"></span>
      <span class="spec-row__value">60-120 m.n.m.</span>
    </div>
    <div class="spec-row spec-row--h76">
      <span class="spec-row__label">processing</span>
      <span class="spec-row__divider"></span>
      <span class="spec-row__value">Unwashed</span>
    </div>
  </section>
</main>
</body>
</html>
```